Modern Business Card

Modern professional business card with more than just logo and demographic info. Something memorable.

We are a trendy/modern chiropractic group with an emphasis on neurology, hence the minimalist-type brain logo. We want to convey that modern and technical aspect with professionalism and the elite nature of our practice environment.

```html
<!DOCTYPE html>
<html lang="en">
<head>
<meta charset="utf-8">
<title>Keystone Spine – Business Card</title>
<link href="https://fonts.googleapis.com/css2?family=Arimo:wght@400;700&display=swap" rel="stylesheet">
<style>
  :root {
    --backdrop: #e6e1d6;
    --card-black: #000000;
    --card-white: #f2f2f2;
    --brand-blue: #3d74bd;
    --ink: #1a1a1a;
    --ink-soft: #555555;
    --wordmark-light: #e9e9e9;
  }
  * { margin: 0; padding: 0; box-sizing: border-box; }
  html, body {
    width: 1200px; height: 960px; overflow: hidden;
    background: var(--backdrop);
    font-family: "Arimo", Arial, sans-serif;
  }
  .sheet {
    position: relative; width: 1200px; height: 960px;
    display: flex; flex-direction: column; align-items: center; justify-content: center; gap: 40px;
  }
  .card {
    position: relative; width: 700px; height: 400px;
    box-shadow: 0 6px 18px rgba(0,0,0,0.18);
  }
  .card--front { background: var(--card-black); }
  .card--back { background: var(--card-white); }

  .wordmark {
    position: absolute; display: flex; align-items: center; gap: 14px;
    font-family: "Arimo", Arial, sans-serif; font-weight: 700;
    letter-spacing: 0.06em; text-transform: uppercase;
  }
  .wordmark__square { width: 34px; height: 34px; background: var(--brand-blue); flex: none; }
  .card--front .wordmark {
    left: 50%; top: 50%; transform: translate(-50%, -50%);
    color: var(--wordmark-light); font-size: 42px;
  }
  .card--back .wordmark {
    left: 70px; top: 95px; color: var(--ink); font-size: 36px;
  }
  .card--back .wordmark__square { width: 30px; height: 30px; }

  .rule {
    position: absolute; left: 175px; right: 70px; top: 232px;
    height: 2px; background: var(--brand-blue);
  }
  .person {
    position: absolute; right: 70px; top: 176px; text-align: right;
  }
  .person__name { font-size: 24px; font-weight: 700; color: var(--ink); line-height: 1.1; }
  .person__role { font-size: 14px; color: var(--ink-soft); margin-top: 4px; }

  .address {
    position: absolute; right: 70px; top: 248px; text-align: right;
    font-size: 15px; line-height: 1.45; color: var(--ink-soft); font-style: normal;
  }
  .contacts {
    position: absolute; left: 175px; top: 248px; list-style: none;
    font-size: 15px; line-height: 1.45; color: var(--ink);
  }
  .contacts li { display: flex; align-items: center; gap: 9px; }
  .contacts svg { width: 13px; height: 13px; fill: var(--brand-blue); flex: none; }
</style>
</head>
<body>
<main class="sheet">
  <section class="card card--front" aria-label="Card front">
    <div class="wordmark"><span class="wordmark__square"></span><span>Keystone Spine</span></div>
  </section>

  <section class="card card--back" aria-label="Card back">
    <div class="wordmark"><span class="wordmark__square"></span><span>Keystone Spine</span></div>

    <div class="person">
      <div class="person__name">Marcus Hale</div>
      <div class="person__role">Owner</div>
    </div>

    <div class="rule"></div>

    <address class="address">
      2210 Larkin Ave<br>
      Suite 40<br>
      Glenfield, MD 21500
    </address>

    <ul class="contacts">
      <li>
        <svg viewBox="0 0 16 16" aria-hidden="true"><path d="M3.5 1l2.5 3-1.5 1.5c.8 2 2.5 3.7 4.5 4.5L10.5 8.5l3 2.5-1.5 3C7 14 2 9 2 2.5z"/></svg>
        410.555.0182
      </li>
      <li>
        <svg viewBox="0 0 16 16" aria-hidden="true"><rect x="4" y="1" width="8" height="4"/><rect x="1" y="6" width="14" height="6" rx="1"/><rect x="4" y="10" width="8" height="5"/></svg>
        410.555.0183
      </li>
      <li>
        <svg viewBox="0 0 16 16" aria-hidden="true"><path d="M1 3h14v10H1z M1 3l7 6 7-6" fill="none" stroke="#3d74bd" stroke-width="1.8"/></svg>
        info@keystonespine.com
      </li>
      <li>
        <svg viewBox="0 0 16 16" aria-hidden="true"><circle cx="8" cy="8" r="6.5" fill="none" stroke="#3d74bd" stroke-width="1.5"/><path d="M1.5 8h13M8 1.5v13" stroke="#3d74bd" stroke-width="1.2"/><ellipse cx="8" cy="8" rx="3" ry="6.5" fill="none" stroke="#3d74bd" stroke-width="1.2"/></svg>
        www.keystonespine.com
      </li>
    </ul>
  </section>
</main>
</body>
</html>
```